Author/ Speaker Business Card design

I need a business card designed that will go with the branding that is already on my book and website. I like clean and straightforward, but I am not opposed to something more 'innovative'.

Target Market(s)

Colleges and Universities, educational institutions

Industry/Entity Type

Education

Contact Information for Business Card

Standard size. It should be able to be printed on good quality white or ivory paper.

Font styles to use
Sans Serif

Colors
0355a3

Requirements
Must have
• There's a blue on my website. It should have some blue. My logo is at the top. It should have the logo incorporated somewhere on it. My name, Author | Speaker | Teacher | Trainer, my phone number (+31 64-207 5184), my email address (milo@thebrightlearner.example), Social media icons (twitter, Instagram, LinkedIn) with the addresses (twitter @writermilohart, Instagram - thebrightlearner, LinkedIn - thebrightlearner) By they way, the website is www.thebrightlearner.example. There is a photo of the book on the website. Also, my full name is Milo Hart
Nice to have
• Try to use the font that is on the website and book. Also, if you could get that blue, that would be great.
Should not have
• My photo

```html
<!DOCTYPE html>
<html lang="en">
<head>
<meta charset="utf-8">
<title>The Bright Learner – Business Card</title>
<link rel="stylesheet" href="https://fonts.googleapis.com/css2?family=Mulish:wght@800&family=Questrial&display=swap">
<style>
  :root {
    --brand-blue: #0355a3;
    --ink: #1a1a1a;
    --muted: #3a3a3a;
    --paper: #ffffff;
    --backdrop: #d9dadc;
  }
  * { margin: 0; padding: 0; box-sizing: border-box; }
  html, body {
    width: 1200px; height: 1000px; overflow: hidden;
    background: var(--backdrop);
  }
  .card {
    position: absolute;
    left: 150px; top: 243px;
    width: 900px; height: 514px;
    background: var(--paper);
    border-radius: 34px;
    box-shadow: 0 6px 24px rgba(0,0,0,0.12);
    font-family: "Questrial", "Century Gothic", sans-serif;
    color: var(--ink);
  }
  .brand {
    position: absolute;
    left: 70px; top: 200px;
    width: 310px;
    display: flex; align-items: center; gap: 14px;
  }
  .brand-dot {
    width: 46px; height: 46px; flex: none;
    border-radius: 50%;
    background: var(--brand-blue);
  }
  .brand-name {
    font-family: "Questrial", "Century Gothic", sans-serif;
    font-size: 38px; line-height: 1.0;
    color: var(--brand-blue);
  }
  .divider {
    position: absolute;
    left: 420px; top: 128px;
    width: 3px; height: 250px;
    background: var(--brand-blue);
  }
  .contact {
    position: absolute;
    left: 448px; top: 126px;
  }
  .person-name {
    font-family: "Mulish", "Century Gothic", sans-serif;
    font-weight: 800;
    font-size: 31px;
    color: var(--brand-blue);
    letter-spacing: 0.5px;
  }
  .roles {
    font-size: 17px; color: var(--muted);
    margin-top: 4px; letter-spacing: 0.6px;
  }
  .details { list-style: none; margin-top: 22px; }
  .details li {
    display: flex; align-items: center; gap: 9px;
    font-size: 22px; line-height: 33px;
  }
  .details svg { width: 18px; height: 18px; flex: none; }
  .icon-dot {
    width: 16px; height: 16px; flex: none; margin: 0 1px;
    border-radius: 50%; background: var(--brand-blue);
  }
  .url-domain { color: var(--brand-blue); font-weight: 700; }
</style>
</head>
<body>
  <main class="card">
    <div class="brand">
      <span class="brand-dot" aria-hidden="true"></span>
      <span class="brand-name">The Bright<br>Learner</span>
    </div>

    <div class="divider" aria-hidden="true"></div>

    <section class="contact">
      <h1 class="person-name">Milo Hart</h1>
      <p class="roles">Author | Speaker | Teacher | Trainer</p>
      <ul class="details">
        <li>
          <svg viewBox="0 0 24 24" aria-hidden="true"><path fill="var(--brand-blue)" d="M6.6 10.8a15 15 0 0 0 6.6 6.6l2.2-2.2c.3-.3.7-.4 1-.2 1.1.4 2.3.6 3.6.6.6 0 1 .4 1 1V20c0 .6-.4 1-1 1A17 17 0 0 1 3 4c0-.6.4-1 1-1h3.5c.6 0 1 .4 1 1 0 1.3.2 2.5.6 3.6.1.3 0 .7-.2 1z"/></svg>
          <span>+31 64-207 5184</span>
        </li>
        <li>
          <svg viewBox="0 0 24 24" aria-hidden="true"><rect x="2" y="5" width="20" height="14" rx="2" fill="var(--brand-blue)"/><path d="M3 6l9 7 9-7" fill="none" stroke="#fff" stroke-width="1.8"/></svg>
          <span>milo@thebrightlearner.example</span>
        </li>
        <li>
          <span class="icon-dot" aria-hidden="true"></span>
          <span>@writermilohart</span>
        </li>
        <li>
          <span class="icon-dot" aria-hidden="true"></span>
          <span>thebrightlearner</span>
        </li>
        <li>
          <svg viewBox="0 0 24 24" aria-hidden="true"><g fill="none" stroke="var(--brand-blue)" stroke-width="1.8"><circle cx="12" cy="12" r="9"/><ellipse cx="12" cy="12" rx="4" ry="9"/><path d="M3 12h18M5 7h14M5 17h14"/></g></svg>
          <span>www.<span class="url-domain">thebrightlearner</span>.example</span>
        </li>
      </ul>
    </section>
  </main>
</body>
</html>
```